Keelby marketing postcards (6x9)

I would like to replicate this 6x9 postcard, but update name/logo, phone number, web address, etc. I also need to create a second postcard copying this basic design, but with updated content and background pictures. Updated contact info to be used for both postcards:
Website: www.keelbyhomestay.com
Name: Mark Tessler
Email: mtessler@keelbyhomestay.com
Phone: (555) 246-8130

Requirements
Must have
• Need two 6x9 postcard designs; 1 themed for Rivenport College, 1 for Calder State. Have uploaded photos that can be used in design. RC can be used for RC postcard (only), CS can be used for CS (only), Generic can be used for either. I've tried to upload extra photos so that you can use your creativity in selecting those that work best in the design.
Nice to have
• In the "Color palette" file, it has the two color schemes -- one for Rivenport College and one for Calder State. Those respective color schemes should be heavily represented in each design. Then there are different groups of pictures labelled either "CS" or "RC", plus some labelled "Generic". The generic ones can be used in either design, the others should be used only for the design for that school.

```html
<!DOCTYPE html>
<html lang="en">
<head>
<meta charset="utf-8">
<title>Keelby Residential – Postcards</title>
<link rel="stylesheet" href="https://fonts.googleapis.com/css2?family=Archivo+Black&family=Arimo:wght@400;500&family=Oswald:wght@500&family=Roboto+Condensed:wght@700&display=swap">
<style>
  :root {
    --maroon: #5a0028;
    --maroon-deep: #4a0020;
    --brand-blue: #5a6cf2;
    --panel-blue: #5872f6;
    --aqua: #4ed8e0;
    --white: #ffffff;
    --slate-glass: rgba(52, 66, 88, 0.72);
    --mail-red: #e8506a;
    --stage-top: #7d7d7d;
    --stage-bottom: #a9a9a9;
    --hairline: #555;
  }
  * { box-sizing: border-box; margin: 0; padding: 0; }
  html, body { width: 1200px; height: 926px; overflow: hidden; }
  body {
    position: relative;
    background: linear-gradient(160deg, var(--stage-top), var(--stage-bottom));
    font-family: "Arimo", Arial, sans-serif;
  }
  .postcard {
    position: absolute;
    width: 504px;
    height: 336px;
    overflow: hidden;
    background: var(--white);
  }
  .postcard--cs-front { left: 66px; top: 112px; }
  .postcard--rc-front { left: 621px; top: 112px; }
  .postcard--cs-back  { left: 66px; top: 476px; }
  .postcard--rc-back  { left: 620px; top: 476px; }

  .photo { position: absolute; inset: 0; }
  .photo--clocktower {
    background: linear-gradient(180deg, #c58a74 0%, #e6a06e 35%, #8a4a5c 55%, #2a1e1e 72%, #1b1512 100%);
  }
  .photo--capitol {
    background: linear-gradient(180deg, #2f6fc8 0%, #5f8fd0 18%, #4f7a2a 40%, #6f9a3a 62%, #a4a99a 82%, #c9c3b5 100%);
  }

  .brand-bar {
    position: absolute;
    left: 0; top: 24px;
    width: 174px; height: 41px;
    display: flex; align-items: center; gap: 7px;
    padding-left: 17px;
  }
  .postcard--cs-front .brand-bar { background: var(--maroon); }
  .postcard--rc-front .brand-bar { background: var(--slate-glass); }
  .brand-mark {
    width: 12px; height: 12px;
    background: var(--aqua);
    flex: none;
  }
  .brand-name {
    font-family: "Oswald", "Arial Narrow", sans-serif;
    font-weight: 500;
    font-size: 15px;
    letter-spacing: 0.1px;
    color: var(--aqua);
    text-transform: uppercase;
    white-space: nowrap;
  }

  .pitch {
    position: absolute;
    left: 311px; top: 74px;
    width: 180px;
  }
  .rc-glass {
    position: absolute;
    left: 298px; top: 62px;
    width: 206px; height: 126px;
    background: var(--slate-glass);
  }
  .pitch__eyebrow {
    font-family: "Archivo Black", sans-serif;
    font-size: 9.5px;
    line-height: 12px;
    white-space: nowrap;
  }
  .postcard--cs-front .pitch__eyebrow { color: var(--maroon); }
  .postcard--rc-front .pitch__eyebrow { color: var(--aqua); }
  .pitch__headline {
    font-family: "Archivo Black", sans-serif;
    font-size: 18.5px;
    line-height: 20px;
    color: var(--white);
    letter-spacing: 0.3px;
    white-space: nowrap;
  }
  .pitch__note {
    margin-top: 4px;
    width: 162px;
    padding: 5px 6px;
    font-size: 7.4px;
    line-height: 9.5px;
  }
  .postcard--cs-front .pitch__note { background: var(--maroon); color: var(--white); }
  .postcard--rc-front .pitch__note { background: var(--aqua); color: #1d3340; }

  /* back side */
  .tile-grid {
    position: absolute;
    left: 0; top: 0;
    width: 254px; height: 260px;
    display: grid;
    grid-template-columns: 127px 127px;
    grid-template-rows: 130px 130px;
  }
  .tile {
    font-family: "Roboto Condensed", "Arial Narrow", sans-serif;
    font-weight: 700;
    font-size: 8.2px;
    line-height: 10px;
    color: var(--white);
  }
  .postcard--cs-back .tile--copy { background: var(--maroon); }
  .postcard--rc-back .tile--copy { background: var(--panel-blue); }
  .tile--intro { padding: 28px 14px 0 16px; }
  .tile--contact { padding: 33px 12px 0 14px; }
  .tile p + p { margin-top: 10px; }
  .tile--contact p + p { margin-top: 13px; }
  .tile--student { background: linear-gradient(160deg, #e9e6e4, #a9bed6 45%, #7f93ad 70%, #d8d3cf); }
  .tile--watertower { background: linear-gradient(180deg, #e7ecf2 0%, #c9b9a4 40%, #9b6b79 70%, #3f5a34 100%); }
  .tile--campus { background: linear-gradient(180deg, #7fa8cc 0%, #9c8b6a 40%, #5f9a3c 65%, #74b04a 100%); }
  .tile--state-map { background: linear-gradient(135deg, #ffffff 20%, #1f2f7a 45%, #ffffff 60%, #d0142c 80%, #ffffff 95%); }

  .return-block {
    position: absolute;
    left: 263px; top: 28px;
    width: 158px;
    text-align: center;
  }
  .return-block .brand-name {
    font-size: 16px;
    display: flex; align-items: center; justify-content: center; gap: 6px;
  }
  .return-block .brand-mark { display: inline-block; width: 11px; height: 11px; }
  .return-block__line {
    font-size: 8px;
    line-height: 11px;
    font-weight: 500;
  }
  .return-block__line:first-of-type { margin-top: 4px; }
  .postcard--cs-back .return-block__line { color: var(--maroon-deep); }
  .postcard--rc-back .return-block__line { color: var(--brand-blue); }

  .stamp-box {
    position: absolute;
    left: 431px; top: 22px;
    width: 60px; height: 60px;
    border: 0.8px solid var(--hairline);
  }
  .mailing-area {
    position: absolute;
    left: 268px; top: 197px;
    width: 219px; height: 79px;
    border: 0.8px dashed var(--mail-red);
    display: flex; align-items: center; justify-content: center;
    font-size: 8px;
    font-weight: 500;
    color: var(--mail-red);
    letter-spacing: 0.1px;
  }
  .agent-footer {
    position: absolute;
    left: 0; top: 279px;
    width: 254px;
    text-align: center;
    font-size: 8px;
    line-height: 13px;
    font-weight: 500;
    white-space: nowrap;
  }
  .postcard--cs-back .agent-footer { color: var(--maroon-deep); }
  .postcard--rc-back .agent-footer { color: var(--brand-blue); }
  .dot { font-size: 6px; vertical-align: 1px; padding: 0 1px; }
</style>
</head>
<body>

  <!-- Calder State front -->
  <section class="postcard postcard--cs-front">
    <div class="photo photo--clocktower" role="img" aria-label="Campus clock tower at dusk with city lights below an orange sky"></div>
    <div class="brand-bar">
      <span class="brand-mark"></span>
      <span class="brand-name">Keelby Residential</span>
    </div>
    <div class="pitch">
      <p class="pitch__eyebrow">Calder State families</p>
      <h1 class="pitch__headline">Let us help you<br>save thousands<br>on tuition costs</h1>
      <p class="pitch__note">We have been helping out-of-state families gain Texas residency for over 14 years.</p>
    </div>
  </section>

  <!-- Rivenport College front -->
  <section class="postcard postcard--rc-front">
    <div class="photo photo--capitol" role="img" aria-label="Domed capitol building framed by green trees along a walkway under blue sky"></div>
    <div class="brand-bar">
      <span class="brand-mark"></span>
      <span class="brand-name">Keelby Residential</span>
    </div>
    <div class="rc-glass"></div>
    <div class="pitch">
      <p class="pitch__eyebrow">Rivenport College families</p>
      <h1 class="pitch__headline">Let us help you<br>save thousands<br>on tuition costs</h1>
      <p class="pitch__note">We have been helping out-of-state families gain Texas residency for over 14 years.</p>
    </div>
  </section>

  <!-- Calder State back -->
  <section class="postcard postcard--cs-back">
    <div class="tile-grid">
      <div class="tile tile--copy tile--intro">
        <p>Calder parents, did you know you can save over $13,800 a semester in tuition?</p>
        <p>Establishing Texas residency through a property purchase is as easy as 1-2-3.</p>
      </div>
      <div class="tile tile--student" role="img" aria-label="Student in a denim jacket carrying books and a backpack"></div>
      <div class="tile tile--watertower" role="img" aria-label="Campus water tower with a welcome sign behind flowering shrubs"></div>
      <div class="tile tile--copy tile--contact">
        <p>Contact us to learn how we have helped more than 500 families - and counting - save thousands on tuition.</p>
        <p>Lets us help you too.</p>
      </div>
    </div>
    <div class="return-block">
      <div class="brand-name"><span class="brand-mark"></span>Keelby Residential</div>
      <p class="return-block__line">(555) 246-8130</p>
      <p class="return-block__line">www.keelbyhomestay.com</p>
    </div>
    <div class="stamp-box"></div>
    <div class="mailing-area">FOR MAILING ADDRESS ONLY</div>
    <div class="agent-footer">
      <p>Mark Tessler <span class="dot">•</span> Larkfield Realty <span class="dot">•</span> (555) 246-8130</p>
      <p>www.keelbyhomestay.com <span class="dot">•</span> mtessler@keelbyhomestay.com</p>
    </div>
  </section>

  <!-- Rivenport College back -->
  <section class="postcard postcard--rc-back">
    <div class="tile-grid">
      <div class="tile tile--copy tile--intro">
        <p>Rivenport parents, did you know you can save over $13,800 a semester in tuition?</p>
        <p>Establishing Texas residency through a property purchase is as easy as 1-2-3.</p>
      </div>
      <div class="tile tile--campus" role="img" aria-label="Rivenport College tower behind a wide green lawn and trees"></div>
      <div class="tile tile--state-map" role="img" aria-label="State outline filled with a blue, white and red flag design"></div>
      <div class="tile tile--copy tile--contact">
        <p>Contact us to learn how we have helped more than 500 families - and counting - save thousands on tuition.</p>
        <p>Lets us help you too.</p>
      </div>
    </div>
    <div class="return-block">
      <div class="brand-name"><span class="brand-mark"></span>Keelby Residential</div>
      <p class="return-block__line">(555) 246-8130</p>
      <p class="return-block__line">www.keelbyhomestay.com</p>
    </div>
    <div class="stamp-box"></div>
    <div class="mailing-area">FOR MAILING ADDRESS ONLY</div>
    <div class="agent-footer">
      <p>Mark Tessler <span class="dot">•</span> Larkfield Realty <span class="dot">•</span> (555) 246-8130</p>
      <p>www.keelbyhomestay.com <span class="dot">•</span> mtessler@keelbyhomestay.com</p>
    </div>
  </section>

</body>
</html>
```